NEW HIP COOL PROGRESSIVE FUN PPE BUSINESS IN NEED OF STANDOUT ADS

Design a banner ad that is cool, hip, and happening related to PPE. We have a healthcare business that is uber conservative and we have all the "proper" and dull ads to represent the seriousness of our true mission and passion. tidelark.com is an e-commerce non-medical PPE business based in Hawaii. We are ready to share our brand with more people online. Help us create something fun and progressive. Get inspiration from our under construction e-commerce store....tidelark.com

Target Market(s)

BUSINESSES IN NEED OF PPE OPENING UP, FAMILIES AND INDIVIDUALS IN NEED OF PPE, SCHOOLS IN NEED OF PPE.

Industry/Entity Type

Medical Supply

Font styles to use
Serif
Sans Serif

Requirements
Must have
• Add some hawaiian or local flair. Don't make it look so clinical. This is a site for consumers and businesses.

```html
<!DOCTYPE html>
<html lang="en">
<head>
<meta charset="utf-8">
<title>Banner ad designs – tidelark.com</title>
<link rel="stylesheet" href="https://fonts.googleapis.com/css2?family=Poppins:wght@600;700&family=Montserrat:wght@400;500;600;700&family=Kalam:wght@400&display=swap">
<style>
  :root {
    --page-bg: #d4f7ea;
    --banner-light: #a8f2d3;
    --banner-mid: #6de8bb;
    --banner-deep: #35dca2;
    --tag-green: #128a42;
    --logo-green: #0f6e33;
    --ink: #0b0b0b;
    --body-grey: #4a4a4a;
    --white: #ffffff;
    --product-blue: #8fd2e6;
    --product-white: #f2f6f8;
  }
  * { margin: 0; padding: 0; box-sizing: border-box; }
  html, body { width: 1200px; height: 1150px; overflow: hidden; }
  body { background: var(--page-bg); font-family: "Montserrat", Arial, sans-serif; color: var(--ink); position: relative; }

  .banner {
    position: absolute;
    overflow: hidden;
    background:
      radial-gradient(circle at 70% 40%, rgba(255,255,255,0.35), rgba(255,255,255,0) 45%),
      linear-gradient(135deg, var(--banner-light) 0%, var(--banner-mid) 55%, var(--banner-deep) 100%);
    box-shadow: 6px 8px 10px rgba(0,0,0,0.22);
  }
  .banner > * { position: absolute; }

  .headline { font-family: "Poppins", Arial, sans-serif; font-weight: 700; letter-spacing: -0.5px; }
  .origin-tag {
    background: var(--tag-green); color: var(--white);
    font-family: "Montserrat", Arial, sans-serif; font-weight: 500;
    display: flex; align-items: center; justify-content: center; white-space: nowrap;
  }
  .ship-note { font-family: "Kalam", "Comic Sans MS", cursive; }
  .brand-name { font-family: "Montserrat", Arial, sans-serif; font-weight: 700; color: var(--logo-green); white-space: nowrap; }
  .selling-points { font-family: "Montserrat", Arial, sans-serif; font-weight: 500; }
  .order-button {
    background: var(--ink); color: var(--white);
    font-family: "Montserrat", Arial, sans-serif; font-weight: 500;
    display: flex; align-items: center; justify-content: center; white-space: nowrap;
  }
  .product-shot {
    border-radius: 18px;
    background: linear-gradient(100deg, var(--product-blue) 0%, #b7e4f0 48%, var(--product-white) 52%, #dfe8ec 100%);
    opacity: 0.9;
  }

  /* Leaderboard 988 x 122 */
  .leaderboard { left: 115px; top: 84px; width: 988px; height: 122px; }
  .leaderboard .headline { left: 45px; top: 10px; font-size: 30px; line-height: 29px; text-align: center; width: 140px; }
  .leaderboard .origin-tag { left: 43px; top: 84px; width: 148px; height: 18px; font-size: 11px; }
  .leaderboard .ship-note { left: 235px; top: 30px; font-size: 15px; line-height: 21px; }
  .leaderboard .product-shot { left: 333px; top: 10px; width: 160px; height: 102px; }
  .leaderboard .brand-name { left: 520px; top: 52px; font-size: 17px; }
  .leaderboard .selling-points { left: 646px; top: 34px; width: 200px; font-size: 13.5px; line-height: 18px; }
  .leaderboard .order-button { left: 832px; top: 42px; width: 135px; height: 37px; font-size: 14px; }

  /* Skyscraper 407 x 814 */
  .skyscraper { left: 117px; top: 244px; width: 407px; height: 814px; }
  .skyscraper .headline { left: 0; width: 407px; top: 30px; font-size: 66px; line-height: 66px; text-align: center; }
  .skyscraper .origin-tag { left: 98px; top: 181px; width: 212px; height: 27px; font-size: 17px; }
  .skyscraper .ship-note { left: 0; width: 407px; top: 226px; font-size: 22px; line-height: 32px; text-align: center; }
  .skyscraper .product-shot { left: 30px; top: 310px; width: 340px; height: 200px; }
  .skyscraper .brand-name { left: 0; width: 407px; top: 583px; font-size: 25px; text-align: center; }
  .skyscraper .selling-points { left: 30px; width: 347px; top: 640px; font-size: 18px; line-height: 31px; text-align: center; }
  .skyscraper .order-button { left: 136px; top: 740px; width: 136px; height: 38px; font-size: 15px; }

  /* Medium rectangle 456 x 380 */
  .medium-rectangle { left: 567px; top: 244px; width: 456px; height: 380px; }
  .medium-rectangle .headline { left: 30px; top: 20px; width: 200px; font-size: 40px; line-height: 40px; text-align: center; }
  .medium-rectangle .origin-tag { left: 42px; top: 111px; width: 154px; height: 19px; font-size: 12px; }
  .medium-rectangle .ship-note { left: 58px; top: 136px; font-size: 16px; line-height: 22px; }
  .medium-rectangle .brand-name { left: 298px; top: 70px; font-size: 20px; }
  .medium-rectangle .selling-points { left: 274px; width: 160px; top: 122px; font-size: 16px; line-height: 24px; text-align: right; }
  .medium-rectangle .product-shot { left: 45px; top: 190px; width: 250px; height: 165px; }
  .medium-rectangle .order-button { left: 298px; top: 318px; width: 136px; height: 37px; font-size: 14px; }

  /* Presentation copy */
  .showcase-title { position: absolute; left: 583px; top: 726px; font-family: "Poppins", Arial, sans-serif; font-weight: 600; font-size: 48px; letter-spacing: -0.5px; }
  .showcase-copy { position: absolute; left: 583px; width: 540px; font-size: 16.5px; line-height: 24px; color: var(--body-grey); }
  .showcase-copy.first { top: 814px; }
  .showcase-copy.second { top: 912px; }
</style>
</head>
<body>

  <section class="banner leaderboard" aria-label="Leaderboard banner">
    <h2 class="headline">safety supplies</h2>
    <div class="origin-tag">from Hawaii for Hawaii</div>
    <p class="ship-note">but we'll<br>ship to<br>anyone!</p>
    <div class="product-shot" role="img" aria-label="Blue disposable face mask beside a clear face shield"></div>
    <div class="brand-name">tidelark.com</div>
    <p class="selling-points">hawaii-based, ships fast, local pick-up &amp; delivery available!</p>
    <div class="order-button">ORDER NOW</div>
  </section>

  <section class="banner skyscraper" aria-label="Skyscraper banner">
    <h2 class="headline">safety<br>supplies</h2>
    <div class="origin-tag">from Hawaii for Hawaii</div>
    <p class="ship-note">but we'll ship to<br>anyone!</p>
    <div class="product-shot" role="img" aria-label="Blue disposable face mask beside a clear face shield"></div>
    <div class="brand-name">tidelark.com</div>
    <p class="selling-points">hawaii-based, ships fast, local pick-up &amp; delivery available!</p>
    <div class="order-button">ORDER NOW</div>
  </section>

  <section class="banner medium-rectangle" aria-label="Medium rectangle banner">
    <h2 class="headline">safety<br>supplies</h2>
    <div class="origin-tag">from Hawaii for Hawaii</div>
    <p class="ship-note">but we'll ship to<br>anyone!</p>
    <div class="brand-name">tidelark.com</div>
    <p class="selling-points">hawaii-based, ships fast, local pick-up &amp; delivery available!</p>
    <div class="product-shot" role="img" aria-label="Blue disposable face mask beside a clear face shield"></div>
    <div class="order-button">ORDER NOW</div>
  </section>

  <h1 class="showcase-title">banner ad designs</h1>
  <p class="showcase-copy first">Contrary to popular belief, Lorem Ipsum is not simply random text. It has roots in a piece of classical Latin literature from 45 BC, making it over 2000 years old.</p>
  <p class="showcase-copy second">Contrary to popular belief, Lorem Ipsum is not simply random text. It has roots in a piece of classical Latin literatur</p>

</body>
</html>
```